Velmira sailing boat for love and romance seekers*

We will pay extra 200$ for the winning design! So, we have a sailing boat, Harlow 58 KT called Velmira, which we’d like to give for charter in Turkey and maybe other countries. Need a dedicated web page, with gallery, calendar, videos, customer reviews, possibility to pay down payment, legal disclosures and in 3 languages (English, Russian and Turkish). Also, there should be info on toys and crew. We can also agree on a monthly fee for maintenance and updates. It’s really important to show the details, so that potential customers can see clearly that the boat is in perfect shape. If needed, we can even make a 3D of the interior, or any other materials that you might need. People should also have the possibility to see the sailing routes that they can chose and experience while cruising. Additionally, we can organize diving tours, surfing lessons, and any other activities.

Target Market(s)

Family with kids. Those people that are looking for more luxury than what’s usually offered with other boats. This is a middle segment between usual boats and super luxury boats. Also, it’s for those people that want romance, love and are looking for Unforgetable experiences with their family.

Coding

Coded - Design and coding required

Number of Pages Required

3 page

Font styles to use
Sans Serif

Requirements
Must have
• Boat has lots of options, and we have a tender boat with which one can waterski, pull ringos and other toys. It’s big enough to carry all guests at the same time and comfortable to reach safely any remote beach location. We have brand new snorkeling and diving equipment, new paddle and surfing boards, new dartino, Gorvetto and life jackets for all age groups. Also, we should have a page on crew, who they are and whom additionally they can chose (for example cook or cleaning staff).
Nice to have
• We’d like to see a page with will make you dream, feel romantic and in love. To ensure the visitors that our boat is perfect for a dream holiday. Imagine being in a secluded white sand beach bay all alone with your loved ones, in a beautiful luxurious boat. Now stop dreaming and join us to make your dreams come true. Lastly, because of virus, we should also mention that we do proper cleaning of boat after every use (COVID free).

Vēlmirā is a Sanskrit word that means "wandering" or "world", with the connotation of cyclic, circuitous change. It is also the concept of rebirth and "cyclicality of all life, matter, existence", a fundamental belief of most Indian religions. In short, it is the cycle of death and rebirth.
Should not have
• It should not be only for one system, all devices should be able to see that page properly.

```html
<!DOCTYPE html>
<html lang="en">
<head>
<meta charset="utf-8">
<title>Velmira — Sailing Charter</title>
<link rel="stylesheet" href="https://fonts.googleapis.com/css2?family=Oswald:wght@300;400;500&family=Montserrat:wght@400;500;800&display=swap">
<style>
  :root {
    --page-bg: #eceef1;
    --navy: #03283a;
    --accent: #0a9fd9;
    --accent-light: #43c6f2;
    --white: #ffffff;
    --muted: rgba(255,255,255,0.62);
    --faint: rgba(255,255,255,0.16);
    --rule: rgba(255,255,255,0.28);
    --display: "Oswald", sans-serif;
    --body: "Montserrat", sans-serif;
  }
  * { box-sizing: border-box; margin: 0; padding: 0; }
  html, body { width: 673px; height: 1200px; overflow: hidden; }
  body { background: var(--page-bg); position: relative; font-family: var(--body); color: var(--white); }

  .screen { position: absolute; left: 31px; width: 611px; height: 380px; overflow: hidden; }
  .screen--home { top: 15px; }
  .screen--menu { top: 410px; background: var(--navy); }
  .screen--about { top: 805px; }

  .brand { position: absolute; left: 19px; top: 17px; font-family: var(--display); font-weight: 400; font-size: 19px; letter-spacing: 1px; color: var(--white); }
  .menu-toggle { position: absolute; right: 20px; top: 20px; width: 20px; height: 18px; }

  .hero-photo { position: absolute; inset: 0; background: linear-gradient(180deg, #6b8db5 0%, #3d5a36 10%, #4e6a3e 40%, #b8b8a8 64%, #2fb4c9 72%, #128fc4 100%); }
  .hero-title { position: absolute; left: 0; right: 0; top: 153px; text-align: center; font-family: var(--display); font-weight: 300; font-size: 16.5px; line-height: 23px; letter-spacing: 0.2px; text-transform: uppercase; }
  .hero-button { position: absolute; left: 262px; top: 211px; width: 86px; height: 16px; border: 1px solid var(--rule); font-size: 6px; letter-spacing: 0.8px; text-align: center; line-height: 14px; color: var(--accent-light); text-transform: uppercase; font-weight: 500; }
  .scroll-cue { position: absolute; left: 582px; width: 10px; height: 20px; }

  .close { position: absolute; right: 20px; top: 19px; display: flex; align-items: center; gap: 6px; font-family: var(--display); font-size: 9px; letter-spacing: 0.5px; }
  .nav { position: absolute; right: 21px; top: 55px; text-align: right; list-style: none; }
  .nav li { height: 41px; }
  .nav .label { display: block; font-family: var(--body); font-weight: 800; font-size: 21px; line-height: 23px; color: var(--accent); letter-spacing: 0.3px; }
  .nav .sub { display: block; font-size: 6.5px; line-height: 8px; color: var(--muted); }
  .contact { position: absolute; right: 21px; top: 266px; text-align: right; font-family: var(--display); font-size: 8px; line-height: 12px; color: var(--accent-light); }
  .langs { position: absolute; right: 21px; top: 298px; font-family: var(--display); font-size: 8px; font-weight: 500; }
  .langs .current { position: relative; }
  .langs .current::before { content: ""; position: absolute; left: 3px; top: -4px; width: 3px; height: 3px; border-radius: 50%; background: var(--white); }
  .legal { position: absolute; right: 21px; top: 338px; font-family: var(--display); font-size: 6px; letter-spacing: 0.3px; color: var(--accent); }
  .socials { position: absolute; right: 21px; top: 359px; display: flex; gap: 4px; }
  .socials span { width: 12px; height: 12px; border: 1px solid var(--muted); border-radius: 50%; }

  .about-photo { position: absolute; inset: 0; background: linear-gradient(180deg, #2b2e31 0%, #303234 45%, #3a3329 70%, #5a4326 85%, #2d261f 100%); }
  .section-ghost { position: absolute; left: 479px; top: 40px; font-family: var(--display); font-size: 26px; color: var(--faint); }
  .about-frame { position: absolute; left: 382px; top: 81px; width: 163px; height: 131px; border: 1px solid var(--rule); }
  .about-image { position: absolute; left: 375px; top: 73px; width: 162px; height: 131px; background: linear-gradient(160deg, #8d8f8c 0%, #d9b36a 45%, #c9c2b3 70%, #4b4a47 100%); }
  .subnav { position: absolute; left: 66px; top: 156px; list-style: none; font-family: var(--display); font-size: 8px; }
  .subnav li { height: 22px; color: var(--muted); }
  .subnav .active { color: var(--white); }
  .subnav .active::before { content: ""; position: absolute; left: -8px; top: 3px; border-left: 4px solid var(--accent-light); border-top: 3px solid transparent; border-bottom: 3px solid transparent; }
  .block-title { position: absolute; font-family: var(--display); font-size: 9px; font-weight: 400; }
  .intro-title { left: 144px; top: 113px; font-size: 14px; }
  .intro-rule { position: absolute; left: 144px; top: 139px; width: 231px; height: 1px; background: var(--rule); }
  .copy { position: absolute; font-size: 5.6px; line-height: 10.6px; color: var(--muted); }
  .intro-copy { left: 144px; top: 154px; width: 206px; }
  .pillars-rule { position: absolute; left: 144px; top: 262px; width: 394px; height: 1px; background: var(--rule); }
  .pillar-copy { top: 276px; width: 106px; }
  .pillar-copy--strong { color: var(--white); font-weight: 500; }
</style>
</head>
<body>

<section class="screen screen--home">
  <div class="hero-photo" role="img" aria-label="Aerial view of a sailing yacht anchored in a turquoise bay below wooded hills"></div>
  <div class="brand">VELMIRA</div>
  <svg class="menu-toggle" viewBox="0 0 20 18" aria-hidden="true"><g fill="#fff"><rect x="0" y="0" width="20" height="2"/><rect x="6" y="5" width="14" height="2"/><rect x="3" y="10" width="17" height="2"/><rect x="0" y="15" width="20" height="2"/></g></svg>
  <h1 class="hero-title">Velmira is perfectly built for a dream holiday and<br>an unforgettable experiences with your family</h1>
  <div class="hero-button">Learn more</div>
  <svg class="scroll-cue" style="top:188px" viewBox="0 0 10 20" aria-hidden="true"><g fill="none" stroke="#43c6f2" stroke-width="1.2"><rect x="2" y="1" width="6" height="7"/><line x1="5" y1="8" x2="5" y2="18"/><polyline points="2,15 5,18 8,15"/></g></svg>
</section>

<section class="screen screen--menu">
  <div class="brand">VELMIRA</div>
  <div class="close">CLOSE
    <svg width="22" height="22" viewBox="0 0 22 22" aria-hidden="true"><g stroke="#fff" stroke-width="1"><line x1="1" y1="1" x2="21" y2="21"/><line x1="21" y1="1" x2="1" y2="21"/></g></svg>
  </div>
  <ul class="nav">
    <li><span class="label">ABOUT</span><span class="sub">Who We Are</span></li>
    <li><span class="label">CALENDAR</span><span class="sub">What We Offer</span></li>
    <li><span class="label">GALLERY</span><span class="sub">Latest Experience</span></li>
    <li><span class="label">REVIEWS</span><span class="sub">What People Say</span></li>
    <li><span class="label">CONTACT</span><span class="sub">Get in Touch</span></li>
  </ul>
  <div class="contact">INFO@VELMIRA.COM<br>1800.555.0142</div>
  <div class="langs"><span class="current">EN</span> - TR - RU</div>
  <div class="legal">PRIVACY POLICY - TERMS OF USE</div>
  <div class="socials"><span></span><span></span><span></span><span></span><span></span></div>
</section>

<section class="screen screen--about">
  <div class="about-photo" role="img" aria-label="Yacht deck and rigging at sunset over a calm bay with distant hills"></div>
  <div class="brand">VELMIRA</div>
  <svg class="menu-toggle" viewBox="0 0 20 18" aria-hidden="true"><g fill="#fff"><rect x="0" y="0" width="20" height="2"/><rect x="6" y="5" width="14" height="2"/><rect x="3" y="10" width="17" height="2"/><rect x="0" y="15" width="20" height="2"/></g></svg>
  <div class="section-ghost">ABOUT</div>
  <div class="about-frame"></div>
  <div class="about-image" role="img" aria-label="Yacht helm and cockpit seating in golden sunset light"></div>
  <ul class="subnav">
    <li class="active">VELMIRA</li>
    <li>TEAM</li>
  </ul>
  <h2 class="block-title intro-title">VELMIRA</h2>
  <div class="intro-rule"></div>
  <p class="copy intro-copy">Lorem ipsum dolor sit amet, consectetur adipiscing elit, sed do eiusmod tempor incididunt ut labore et dolore magna aliqua. Ut enim ad minim veniam, quis nostrud exercitation ullamco laboris nisi ut aliquip ex ea commodo consequat. Duis aute irure dolor in reprehenderit in voluptate velit esse cillum dolore eu fugiat nulla pariatur.</p>
  <svg class="scroll-cue" style="top:175px" viewBox="0 0 10 28" aria-hidden="true"><g fill="none" stroke="#43c6f2" stroke-width="1.2"><polyline points="2,4 5,1 8,4"/><line x1="5" y1="1" x2="5" y2="10"/><rect x="2" y="10" width="6" height="7"/><line x1="5" y1="17" x2="5" y2="27"/><polyline points="2,24 5,27 8,24"/></g></svg>
  <h3 class="block-title" style="left:144px;top:248px">MISSION</h3>
  <h3 class="block-title" style="left:285px;top:248px">VISION</h3>
  <h3 class="block-title" style="left:426px;top:248px">VALUES</h3>
  <div class="pillars-rule"></div>
  <p class="copy pillar-copy" style="left:144px">Excepteur sint occaecat cupidatat non proident, sunt in culpa qui officia deserunt mollit.</p>
  <p class="copy pillar-copy" style="left:285px">Lorem ipsum dolor sit amet, consectetur adipiscing elit, sed do eius mod tempor incididunt.</p>
  <p class="copy pillar-copy pillar-copy--strong" style="left:426px">Ut enim ad minim veniam, quis nostrud exercitation ullamco laboris nisi ut aliquip ex ea,</p>
</section>

</body>
</html>
```